Just Sold Postcard

Real Estate/ Thornwick Dale Realty.I'd like a template that I can use to change out the picture of the home, verbiage on the front, and address. I'm including a picture of what I've used in the past. I like designs that use red, with some blue and white. I'd like the ability to change the verbiage on the back as well.

Industry/Entity Type

Real Estate

Font styles to use
Serif
Sans Serif

```html
<!DOCTYPE html>
<html lang="en">
<head>
<meta charset="utf-8">
<title>Just Sold Postcard – Thornwick Dale Realty</title>
<link rel="stylesheet" href="https://fonts.googleapis.com/css2?family=Mulish:wght@400;600;700;800&family=Tinos&display=swap">
<style>
  :root {
    --page-bg: #efece6;
    --brand-red: #d4282b;
    --brand-blue: #1d5ba8;
    --brand-navy: #1f4c95;
    --paper: #ffffff;
    --ink: #1b1b1b;
    --stamp-line: #a9a9a9;
    --photo-sky: #b9d6ea;
    --photo-house: #8e8f86;
    --photo-lawn: #5c8a3a;
  }
  * { box-sizing: border-box; margin: 0; padding: 0; }
  html, body { width: 1200px; height: 1000px; overflow: hidden; }
  body {
    background: var(--page-bg);
    font-family: "Mulish", Arial, sans-serif;
    position: relative;
  }
  .postcard {
    position: absolute;
    top: 109px;
    width: 403px;
    height: 312px;
    background: var(--paper);
    overflow: hidden;
    box-shadow: 0 2px 6px rgba(0,0,0,.18);
  }
  .postcard--front { left: 155px; }
  .postcard--back { left: 628px; }

  /* front */
  .listing-photo {
    position: absolute; left: 0; top: 0; width: 403px; height: 203px;
    background: linear-gradient(180deg, var(--photo-sky) 0%, #cfdfe6 35%, var(--photo-house) 55%, #7b8a6a 78%, var(--photo-lawn) 100%);
  }
  .sold-ribbon { position: absolute; right: 0; top: 0; }
  .listing-band {
    position: absolute; left: 0; top: 203px; width: 403px; height: 47px;
    background: linear-gradient(180deg, #2466b5, var(--brand-blue));
    color: #fff; font-size: 9.5px; font-weight: 700;
    text-align: center; padding-top: 20px;
  }
  .listing-address {
    position: absolute; left: 115px; top: 192px; width: 186px; height: 22px;
    background: #fff; border-radius: 7px;
    font-size: 11.5px; font-weight: 700; color: var(--ink);
    text-align: center; line-height: 22px;
  }
  .agent-block {
    position: absolute; left: 30px; top: 256px; width: 165px; text-align: center;
  }
  .agent-block__name { color: var(--brand-red); font-size: 16px; font-weight: 800; line-height: 19px; }
  .agent-block__tag { color: var(--brand-navy); font-size: 11px; font-weight: 700; line-height: 15px; }
  .agent-block__phone { color: var(--brand-navy); font-size: 11px; font-weight: 700; line-height: 15px; }
  .brokerage {
    position: absolute; right: 20px; top: 268px;
    display: flex; align-items: center; gap: 5px;
  }
  .brokerage__mark { width: 11px; height: 11px; background: var(--brand-red); flex: none; }
  .brokerage__name { color: var(--brand-navy); font-size: 12.5px; font-weight: 700; white-space: nowrap; }

  /* back */
  .contact-panel {
    position: absolute; left: 0; top: 0; width: 195px; height: 258px;
    background: var(--brand-red); color: #fff; text-align: center;
  }
  .contact-panel__intro { position: absolute; top: 75px; left: 0; width: 100%; font-size: 9.5px; line-height: 12.5px; }
  .contact-panel__name { position: absolute; top: 123px; left: 0; width: 100%; font-size: 20px; font-weight: 800; }
  .contact-panel__phone { position: absolute; top: 147px; left: 0; width: 100%; font-size: 17px; }
  .contact-panel__cta { position: absolute; top: 175px; left: 0; width: 100%; font-size: 14px; line-height: 15px; }
  .contact-panel__offer { position: absolute; top: 191px; left: 0; width: 100%; font-size: 10.5px; line-height: 13px; padding: 0 14px; }
  .contact-panel__details { position: absolute; top: 222px; left: 0; width: 100%; font-size: 11px; font-weight: 700; line-height: 14px; }
  .postage-indicia {
    position: absolute; left: 305px; top: 13px; width: 86px; height: 86px;
    border: 1px solid var(--stamp-line);
    font-family: "Tinos", "Times New Roman", serif; font-size: 8.5px; line-height: 12px;
    text-align: center; padding-top: 18px; color: var(--ink);
  }
  .recipient {
    position: absolute; left: 225px; top: 143px; width: 150px; text-align: center;
  }
  .recipient__label { font-family: "Tinos", "Times New Roman", serif; font-size: 12px; color: var(--ink); margin-bottom: 10px; }
  .recipient__lines { font-size: 9.5px; line-height: 12px; color: var(--ink); }
</style>
</head>
<body>

<section class="postcard postcard--front" aria-label="Postcard front">
  <div class="listing-photo" role="img" aria-label="Photo of the sold home: two-storey stone house with lawn and shrubs"></div>
  <svg class="sold-ribbon" width="403" height="140" viewBox="0 0 403 140" aria-label="Just sold, brought buyer">
    <polygon points="265,0 305,0 403,98 403,138" fill="var(--brand-red)"/>
    <g transform="translate(352,62) rotate(45)" fill="#fff" text-anchor="middle" font-family="Mulish, Arial, sans-serif">
      <text y="-3" font-size="13" font-weight="800">JUST SOLD</text>
      <text y="10" font-size="11">Brought Buyer</text>
    </g>
  </svg>
  <div class="listing-band">Fabulous End Unit with granite countertops and hardwood floors. Private lot</div>
  <div class="listing-address">1172 Alder Crest Lane</div>
  <div class="agent-block">
    <div class="agent-block__name">MARLA QUINN</div>
    <div class="agent-block__tag">Your Neighborhood Expert</div>
    <div class="agent-block__phone">555.214.3380</div>
  </div>
  <div class="brokerage">
    <span class="brokerage__mark"></span>
    <span class="brokerage__name">Thornwick Dale Realty</span>
  </div>
</section>

<section class="postcard postcard--back" aria-label="Postcard back">
  <div class="contact-panel">
    <p class="contact-panel__intro">Lorem ipsum dolor sit amet,<br>consectetur adipiscing elit.<br>Integer nec blandit augue.</p>
    <p class="contact-panel__name">MARLA QUINN</p>
    <p class="contact-panel__phone">(555)214-3380</p>
    <p class="contact-panel__cta">Contact me today!</p>
    <p class="contact-panel__offer">For a DREE Market Analysis of your home!</p>
    <p class="contact-panel__details">555.214.3380 or<br>quinn.marla@example.com</p>
  </div>
  <div class="postage-indicia">FIRST-CLASS MAIL<br>US. POSTAGE PSID<br>ASHFORD, VT<br>PERMIT NO. 27</div>
  <div class="recipient">
    <p class="recipient__label">RECEIPIENT`S ADDRESS</p>
    <p class="recipient__lines">Lorem ipsum dolor sit amet,<br>consectetur adipiscing elit.<br>Integer nec blandit augue.</p>
  </div>
</section>

</body>
</html>
```